Book cover - Rise Above Unease and Bashful Nerves

Book cover for Ebook (Lumora) and wrap around print cover (Printvale) (back, front, and spine)

The book title (may slightly change by end of brief):
(MAIN TITLE) 'Rise Above Unease and Bashful Nerves'
(SUB HEADING) 'A Clear Daily Workbook Guide to Rise Above Unease, Outgrow Timidity and Build Inner Poise'
by Dr Owen Farrby

I would like a bold, stand out cover. Contemporary. I would like to avoid stereotypical images of people looking anxious or worried. I would like the design to be more uplifting and hopeful, rather than focusing on the negative aspect of anxiety, but avoiding cliched photos of people raising their hands in the air, smiling and jumping etc. The cover should appeal to both men and women.

Trim size of book cover (for PrintVale) is 5.25" x 8" back and front with a spine size of 0.477 inches

Reason: I have decided to extend the deadline by 1 more day, not because I am unhappy with the quality of the designs, but because a few designers have contacted me to explain they have had technical difficulties when submitting their files. Thanks everyone for the hard work and great designs.

Target Market(s)

Males and females (16+) who struggle with social anxiety and shyness

Industry/Entity Type

Social

Font styles to use
Serif

Requirements
Must have
• Bold cover that is modern and contemporary. For example, I like these covers:
• http://qvlk.io/8kTz3Pm
• http://qvlk.io/9wHe5Nb
• http://qvlk.io/4jMr7Yc
• http://qvlk.io/6nGs2Lq
• http://qvlk.io/3fVb81t
• http://qvlk.io/7yKd4Ue
• http://qvlk.io/5hWx9Oa
Nice to have
• Open to abstract designs.
Should not have
• No stereotypical pictures of people who look anxious or worried. Avoid cliched photos of people raising their hands in the air, smiling and jumping etc.

```html
<!DOCTYPE html>
<html lang="en">
<head>
<meta charset="utf-8">
<title>Rise Above Unease and Bashful Nerves — Wrap Cover</title>
<link rel="stylesheet" href="https://fonts.googleapis.com/css2?family=Crimson+Pro:wght@400;600;700&family=Oswald:wght@500&display=swap">
<style>
  :root {
    --backdrop: #6a6867;
    --paper: #ffffff;
    --band: #bbb8b7;
    --ink: #111111;
    --placeholder-ink: #8a8a8a;
  }
  html, body {
    margin: 0;
    width: 1200px;
    height: 900px;
    overflow: hidden;
    background: var(--backdrop);
  }
  .wrap-cover {
    position: absolute;
    left: 50px;
    top: 48px;
    width: 1100px;
    height: 803px;
    background: var(--paper);
    overflow: hidden;
    font-family: "Crimson Pro", Georgia, serif;
    color: var(--ink);
  }
  .front-title {
    position: absolute;
    left: 578px;
    top: 0;
    width: 522px;
    height: 803px;
  }
  .front-title text {
    font-family: "Crimson Pro", Georgia, serif;
    font-weight: 700;
    fill: var(--ink);
  }
  .lower-band {
    position: absolute;
    inset: 0;
    width: 1100px;
    height: 803px;
  }
  .lower-band polygon { fill: var(--band); }

  /* Back cover */
  .author-photo {
    position: absolute;
    left: 43px;
    top: 32px;
    width: 112px;
    height: 131px;
    background: #000;
    color: #fff;
    display: flex;
    align-items: center;
    justify-content: center;
    font-family: "Oswald", "Arial Narrow", sans-serif;
    font-weight: 500;
    font-size: 18px;
    letter-spacing: 0.5px;
  }
  .blurb {
    position: absolute;
    margin: 0;
    font-size: 14px;
    line-height: 19.6px;
    text-align: justify;
  }
  .blurb-bio { left: 174px; top: 28px; width: 307px; }
  .blurb-intro { left: 48px; top: 176px; width: 433px; }
  .blurb-outro { left: 48px; top: 462px; width: 433px; }
  .isbn-box {
    position: absolute;
    left: 303px;
    top: 667px;
    width: 172px;
    height: 93px;
    background: var(--paper);
    display: flex;
    align-items: center;
    justify-content: center;
    font-family: "Oswald", "Arial Narrow", sans-serif;
    font-weight: 500;
    font-size: 17px;
    color: var(--placeholder-ink);
  }

  /* Spine */
  .spine-text {
    position: absolute;
    left: 533px;
    width: 45px;
    writing-mode: vertical-rl;
    display: flex;
    align-items: center;
    font-size: 15px;
    font-weight: 600;
    white-space: nowrap;
  }
  .spine-title { top: 21px; letter-spacing: 0.3px; }
  .spine-author { top: 637px; letter-spacing: 0.4px; }

  /* Front cover */
  .front-subtitle {
    position: absolute;
    left: 578px;
    top: 530px;
    width: 522px;
    margin: 0;
    text-align: center;
    font-size: 20px;
    font-weight: 600;
    line-height: 29px;
  }
  .front-author {
    position: absolute;
    left: 578px;
    top: 736px;
    width: 522px;
    margin: 0;
    text-align: center;
    font-size: 31px;
    font-weight: 700;
    letter-spacing: 0.5px;
  }
</style>
</head>
<body>
  <div class="wrap-cover">
    <svg class="front-title" viewBox="0 0 522 803" aria-label="Rise Above Unease and Bashful Nerves">
      <text x="261" y="88" text-anchor="middle" font-size="84" textLength="484" lengthAdjust="spacingAndGlyphs">RISE ABOVE</text>
      <text x="261" y="168" text-anchor="middle" font-size="96" textLength="400" lengthAdjust="spacingAndGlyphs">UNEASE</text>
      <text x="261" y="206" text-anchor="middle" font-size="40" textLength="97" lengthAdjust="spacingAndGlyphs">AND</text>
      <text x="261" y="286" text-anchor="middle" font-size="96" textLength="470" lengthAdjust="spacingAndGlyphs">BASHFUL</text>
      <text x="261" y="370" text-anchor="middle" font-size="96" textLength="440" lengthAdjust="spacingAndGlyphs">NERVES</text>
    </svg>

    <svg class="lower-band" viewBox="0 0 1100 803" aria-hidden="true">
      <polygon points="0,444 1100,385 1100,803 0,803"/>
    </svg>

    <div class="author-photo">PHOTO</div>
    <p class="blurb blurb-bio">Lorem ipsum dolor sit amet, consectetur adipiscing elit, sed do eiusmod tempor incididunt ut labore et dolore magna aliqua. Ut enim ad minim veniam, quis nostrud exercitation ullamco laboris nisi ut aliquip ex ea commodo consequat. Duis aute irure dolor in reprehenderit in voluptate juhi.</p>
    <p class="blurb blurb-intro">Sed ut perspiciatis unde omnis iste natus error sit voluptatem accusantium doloremque laudantium, totam rem aperiam, eaque ipsa quae ab illo inventore veritatis et quasi architecto beatae vitae dicta sunt explicabo. Nemo enim ipsam voluptatem quia voluptas sit aspernatur aut odit aut fugit, sed quia consequuntur magni dolores eos qui ratione voluptatem sequi nesciunt. Neque porro quisquam est, qui dolorem ipsum quia dolor sit amet, consectetur, adipisci velit, sed quia non numquam eius modi tempora incidunt ut.</p>
    <p class="blurb blurb-outro">Sed ut perspiciatis unde omnis iste natus error sit voluptatem accusantium doloremque laudantium, totam rem aperiam, eaque ipsa quae ab illo inventore veritatis et quasi architecto beatae vitae dicta sunt explicabo. Nemo enim ipsam voluptatem quia voluptas sit aspernatur aut odit aut fugit, sed quia consequuntur magni dolores eos qui ratione voluptatem sequi nesciunt. Neque porro quisquam est, qui dolorem ipsum quia dolor sit amet, consectetur, adipisci velit, sed quia non numquam eius modi tempora incidunt ut.</p>
    <div class="isbn-box">ISBN / BARCODE</div>

    <div class="spine-text spine-title">RISE ABOVE UNEASE AND BASHFUL NERVES</div>
    <div class="spine-text spine-author">DR OWEN FARRBY</div>

    <p class="front-subtitle">A Clear Daily Workbook Guide to Rise<br>Above Unease, Outgrow Timidity<br>and Build Inner Poise</p>
    <p class="front-author">DR OWEN FARRBY</p>
  </div>
</body>
</html>
```